Super Greens Label for Supplement Bottle

We want to design a front label for a health supplement bottle. The product is called Leafy Blendbite Chews™. This will be a new product so there is no current website for the product. The focus is on supergreens that taste great and deliver support for energy, digestion, and immune defense.
We want it to be modern, vibrant and appealing.
Bottle size: standard size supplement CLEAR bottle size, with white child resistant cap and the label panel dimensions are 3” x 7”. The label should be primarily white and green, with a touch of red; (see color palettes)/it can also ONLY be white and green. See samples attached.
We are only focused on the front of the bottle design, not on the back, but leave space for the supplement panel and other text on the back.
So the text for the front of the bottle is:
RT Dalloway's
Leafy Blendbite Chews™
Super Greens Blend for:
Energy, Digestion, and Immune Support*
60 Gummies | Dietary Supplement
Raspberry Flavor Gummies
Off to side of the label:
Non-GMO
Vegan Friendly
Plant-Based
Gelatin Free
Colors
Designer to choose colors to be used in the design.
Look and feel
Each slider illustrates characteristics of the customer's brand and the style your logo design should communicate.

```html
<!DOCTYPE html>
<html lang="en">
<head>
<meta charset="UTF-8">
<title>Leafy Blendbite Chews – Front Label</title>
<link href="https://fonts.googleapis.com/css2?family=Anton&family=Nunito:wght@800&display=swap" rel="stylesheet">
<style>
  :root {
    --bg: #f4f4f4;
    --green: #3f9c78;
    --green-deep: #178d65;
    --green-mist: #cfe8de;
    --white: #ffffff;
  }
  * { margin: 0; padding: 0; box-sizing: border-box; }
  html, body { width: 1200px; height: 960px; overflow: hidden; background: var(--bg); }
  .label {
    position: absolute; left: 290px; top: 60px; width: 620px; height: 840px;
    background:
      radial-gradient(ellipse 60% 55% at 45% 45%, var(--white) 55%, rgba(255,255,255,0) 100%),
      linear-gradient(180deg, var(--green-mist), #e6f3ee 60%, var(--white));
    overflow: hidden;
    font-family: "Anton", "Impact", sans-serif;
    box-shadow: 0 10px 30px rgba(0,0,0,0.08);
  }
  .claim-strip {
    position: absolute; right: 24px; top: 0; width: 86px; height: 460px;
    background: var(--green); border-radius: 0 0 43px 43px;
    display: flex; flex-direction: column; align-items: center; justify-content: space-around;
    padding: 14px 0 22px;
  }
  .claim-badge {
    width: 66px; height: 66px; border: 2px solid var(--white); border-radius: 50%;
    display: flex; flex-direction: column; align-items: center; justify-content: center;
    color: var(--white); text-align: center; line-height: 1;
  }
  .claim-badge .word { font-size: 15px; letter-spacing: 0.5px; }
  .claim-badge .small { font-family: "Nunito", sans-serif; font-size: 7px; letter-spacing: 0.6px; margin-top: 3px; }
  .claim-badge .soft { font-family: "Nunito", sans-serif; font-size: 14px; font-weight: 800; }
  .brand-logo {
    position: absolute; left: 40px; top: 80px;
    color: var(--green-deep); font-size: 56px; line-height: 0.98; letter-spacing: 0.5px;
  }
  .product-name {
    position: absolute; left: 40px; top: 212px;
    color: var(--green); font-weight: 400; letter-spacing: -0.5px;
  }
  .product-name .line { display: block; line-height: 0.96; }
  .product-name .line-one { font-size: 132px; }
  .product-name .line-two { font-size: 108px; }
  .product-name .line-three { font-size: 140px; }
  .product-name .mark { font-size: 40px; vertical-align: top; line-height: 1; margin-left: 4px; }
  .benefit-line {
    position: absolute; left: 40px; top: 596px; width: 560px;
    color: var(--green-deep); font-size: 27px; line-height: 1.05;
  }
  .count-band {
    position: absolute; left: 0; top: 672px; width: 100%; height: 140px;
    background: linear-gradient(90deg, var(--green) 0%, var(--green-deep) 55%, var(--green) 100%);
    display: flex; align-items: center; padding-left: 40px; gap: 20px;
  }
  .count-number { color: var(--white); font-size: 112px; line-height: 1; }
  .count-details { display: flex; flex-direction: column; gap: 10px; }
  .flavor-tag {
    background: var(--white); color: var(--green-deep);
    font-size: 30px; padding: 2px 10px; border-radius: 3px; line-height: 1.1;
  }
  .supplement-type { color: var(--white); font-size: 32px; line-height: 1; padding-left: 4px; }
</style>
</head>
<body>
  <main class="label">
    <aside class="claim-strip">
      <div class="claim-badge"><span class="word">NON</span><span class="word">GMO</span></div>
      <div class="claim-badge">
        <svg width="20" height="26" viewBox="0 0 20 26"><path d="M10 1 C18 8 18 18 10 24 C2 18 2 8 10 1Z" fill="none" stroke="#fff" stroke-width="2"/><path d="M10 6 V24" stroke="#fff" stroke-width="1.5"/></svg>
        <span class="small">VEGAN FRIENDLY</span>
      </div>
      <div class="claim-badge"><span class="soft">plant</span><span class="soft">based</span></div>
      <div class="claim-badge"><span class="small">GELATIN</span>
        <svg width="22" height="18" viewBox="0 0 22 18"><path d="M3 12 Q3 2 11 2 Q19 2 19 12 Z" fill="none" stroke="#fff" stroke-width="1.8"/><path d="M1 14 H21 M11 14 V17" stroke="#fff" stroke-width="1.8"/></svg>
        <span class="small">FREE</span>
      </div>
    </aside>

    <h2 class="brand-logo">YOUR LOGO<br>HERE</h2>

    <h1 class="product-name">
      <span class="line line-one">LEAFY</span>
      <span class="line line-two">BLENDBITE</span>
      <span class="line line-three">CHEWS<span class="mark">™</span></span>
    </h1>

    <p class="benefit-line">SUPER GREENS BLEND FOR ENERGY, DIGESTION,<br>AND IMMUNE SUPPORT*</p>

    <section class="count-band">
      <span class="count-number">60</span>
      <div class="count-details">
        <span class="flavor-tag">RASPBERRY FLAVOR GUMMIES</span>
        <span class="supplement-type">DIETARY SUPPLEMENT</span>
      </div>
    </section>
  </main>
</body>
</html>
```